Basic images needed for business powerpoint slides

We need basic images for a powerpoint design. The designs should be clean, modern, simple and easy to read on a screen and if they were printed on paper. The images should not be overly designed (no fancy graphics or ornate fonts), but should still look professional.

Please pay attention to the attachments that have sketches of the images that are needed. In the notes section of the powerpoint slides specifies additional details for each image.

Also, please adhere to the design guidelines that are also uploaded. Only use colors and fonts that are specified. The final images should be similar to the look and feel of the images in the design guidelines.
Updates

Designers -
Thanks for all your submissions! I am reviewing all the designs with my team and will have a decision ready by Sunday evening. If you are submitting any new designs, please submit by Sunday morning EST so my team can review them.

Thanks!

Target Market(s)

business executives

Industry/Entity Type

Business

Requirements
Must have
• Must Have:
- 1. Please see the attached powerpoint for the sketches we would like to have recreated. There are specific notes in each slide with additional details.

2. Please refer to the following pages in the uploaded design guideline document:
Colors - p. 14
- Use either the bright or muted color options as specified in the color scheme on this page

Typography - p. 16-17
- Use either helvetica or arial options

Powerpoint guidelines - p.42
- see for example of the general look and feel of the company

```html
<!DOCTYPE html>
<html lang="en">
<head>
<meta charset="utf-8">
<title>KVRS Stakeholder Circles and Team Structure</title>
<link href="https://fonts.googleapis.com/css2?family=Arimo:ital,wght@0,400;0,700;1,400&family=Oswald:wght@500;700&display=swap" rel="stylesheet">
<style>
  :root {
    --teal: #4fc3c4;
    --purple: #64318f;
    --green: #56b04a;
    --dark-green: #2e743a;
    --orange: #f7931e;
    --blue: #29a8e0;
    --charcoal: #333333;
    --label-gray: #555555;
    --white: #ffffff;
    --ink: #222222;
  }
  html, body { margin: 0; padding: 0; overflow: hidden; background: var(--white); }
  .canvas { width: 1200px; height: 900px; display: block; }
  .ring-label { font-family: 'Arimo', Arial, sans-serif; font-size: 11px; fill: var(--white); text-anchor: middle; }
  .ring-label-small { font-family: 'Arimo', Arial, sans-serif; font-size: 8.5px; fill: var(--white); text-anchor: middle; }
  .ring-number { font-family: 'Arimo', Arial, sans-serif; font-size: 10px; fill: var(--white); }
  .group-code { font-family: 'Arimo', Arial, sans-serif; font-weight: 700; font-size: 16px; fill: var(--white); }
  .specialists { font-family: 'Arimo', Arial, sans-serif; font-size: 12px; fill: var(--white); }
  .clinical { font-family: 'Arimo', Arial, sans-serif; font-size: 11px; fill: var(--white); }
  .segment-note { font-family: 'Arimo', Arial, sans-serif; font-size: 7.5px; fill: var(--white); }
  .section-tag { font-family: 'Arimo', Arial, sans-serif; font-size: 17px; fill: var(--white); }
  .division-title { font-family: 'Oswald', Arial, sans-serif; font-weight: 500; font-size: 15px; fill: var(--white); text-anchor: middle; }
  .team-title { font-family: 'Arimo', Arial, sans-serif; font-size: 11px; fill: var(--white); }
  .team-member { font-family: 'Arimo', Arial, sans-serif; font-size: 10px; fill: var(--white); }
  .scope-label { font-family: 'Arimo', Arial, sans-serif; font-style: italic; font-size: 15px; fill: var(--ink); }
  .swatch-code { font-family: 'Arimo', Arial, sans-serif; font-size: 4px; fill: var(--ink); }
  .swatch-name { font-family: 'Arimo', Arial, sans-serif; font-size: 4px; fill: var(--white); }
</style>
</head>
<body>
<svg class="canvas" viewBox="0 0 1200 900" xmlns="http://www.w3.org/2000/svg">

  <!-- Internal stakeholder circle -->
  <g class="stakeholders-internal">
    <rect x="63" y="62" width="82" height="27" fill="var(--label-gray)"/>
    <text class="section-tag" x="74" y="81">Internal</text>
    <circle cx="341" cy="254" r="214" fill="var(--teal)"/>
    <circle cx="341" cy="254" r="181" fill="var(--purple)"/>
    <circle cx="341" cy="254" r="151" fill="var(--green)"/>
    <circle cx="341" cy="254" r="121" fill="var(--dark-green)"/>
    <line x1="341" y1="134" x2="341" y2="374" stroke="var(--white)" stroke-width="1.5"/>
    <line x1="192" y1="253" x2="490" y2="253" stroke="var(--white)" stroke-width="1.5"/>

    <text class="ring-label" x="339" y="67">Franchise Lawyers | Finance</text>
    <text class="ring-number" x="424" y="80">9</text>
    <text class="ring-label" x="339" y="95">Legal Analysts</text>
    <text class="ring-number" x="390" y="102">8</text>
    <text class="ring-label" x="341" y="128">Sales &amp; Marketing</text>
    <text class="ring-number" x="275" y="138">7</text>
    <text class="ring-label" x="339" y="391">Scientists</text>
    <text class="ring-number" x="376" y="380">6</text>

    <text class="ring-number" x="257" y="203">1</text>
    <text class="group-code" x="286" y="208">KVRS</text>
    <text class="specialists" x="275" y="220">specialists</text>
    <line x1="275" y1="224" x2="329" y2="224" stroke="var(--white)"/>
    <text class="segment-note" x="276" y="234">(Med products -</text>
    <text class="segment-note" x="280" y="244">Commercial)</text>

    <text class="ring-number" x="416" y="203">2</text>
    <text class="group-code" x="350" y="208">KVRS</text>
    <text class="specialists" x="350" y="220">specialists</text>
    <line x1="350" y1="224" x2="404" y2="224" stroke="var(--white)"/>
    <text class="segment-note" x="350" y="234">(Bio Science -</text>
    <text class="segment-note" x="350" y="244">Commercial)</text>

    <text class="ring-number" x="257" y="273">3</text>
    <text class="group-code" x="286" y="278">KVRS</text>
    <text class="specialists" x="275" y="290">specialists</text>
    <line x1="275" y1="294" x2="329" y2="294" stroke="var(--white)"/>
    <text class="segment-note" x="276" y="304">(Med products -</text>
    <text class="segment-note" x="280" y="314">Med Affairs)</text>

    <text class="ring-number" x="416" y="273">4</text>
    <text class="group-code" x="350" y="278">KVRS</text>
    <text class="specialists" x="350" y="290">specialists</text>
    <line x1="350" y1="294" x2="404" y2="294" stroke="var(--white)"/>
    <text class="segment-note" x="350" y="304">(Bio Science -</text>
    <text class="segment-note" x="350" y="314">Med Affairs)</text>

    <text class="clinical" x="350" y="335">Clinical</text>
    <text class="clinical" x="350" y="346">Affairs</text>
    <text class="ring-number" x="399" y="335">5</text>
  </g>

  <!-- External stakeholder circle -->
  <g class="stakeholders-external">
    <rect x="633" y="62" width="84" height="27" fill="var(--label-gray)"/>
    <text class="section-tag" x="646" y="81">External</text>
    <circle cx="910" cy="254" r="214" fill="var(--teal)"/>
    <circle cx="910" cy="254" r="181" fill="var(--purple)"/>
    <circle cx="910" cy="254" r="151" fill="var(--green)"/>
    <circle cx="910" cy="254" r="121" fill="var(--dark-green)"/>
    <line x1="910" y1="260" x2="910" y2="134" stroke="var(--white)" stroke-width="1.5"/>
    <line x1="910" y1="260" x2="785" y2="330" stroke="var(--white)" stroke-width="1.5"/>
    <line x1="910" y1="260" x2="1035" y2="330" stroke="var(--white)" stroke-width="1.5"/>

    <text class="ring-label-small" x="912" y="59">Franchise Lawyers | Finance</text>
    <text class="ring-label-small" x="912" y="69">Comittiee Members</text>
    <text class="ring-number" x="978" y="72">15</text>
    <text class="ring-label" x="912" y="93">Legal Analysts</text>
    <text class="ring-number" x="964" y="104">14</text>
    <text class="ring-label-small" x="914" y="121">Phycisians, Clinicians</text>
    <text class="ring-label-small" x="914" y="131">Scientists</text>
    <text class="ring-number" x="848" y="139">13</text>
    <text class="ring-label" x="914" y="389">External Orgs</text>

    <text class="ring-number" x="883" y="189">10</text>
    <text class="group-code" x="852" y="215">KVRS</text>
    <text class="specialists" x="840" y="227">specialists</text>
    <line x1="840" y1="231" x2="894" y2="231" stroke="var(--white)"/>
    <text class="segment-note" x="840" y="241">(Med products -</text>
    <text class="segment-note" x="840" y="251">Med Affairs)</text>

    <text class="ring-number" x="930" y="189">11</text>
    <text class="group-code" x="932" y="215">KVRS</text>
    <text class="specialists" x="932" y="227">specialists</text>
    <line x1="932" y1="231" x2="986" y2="231" stroke="var(--white)"/>
    <text class="segment-note" x="932" y="241">(Bio Science -</text>
    <text class="segment-note" x="932" y="251">Med Affairs)</text>

    <text class="group-code" x="892" y="294">KVRS</text>
    <text class="specialists" x="891" y="305">specialists</text>
    <line x1="891" y1="309" x2="945" y2="309" stroke="var(--white)"/>
    <text class="segment-note" x="891" y="320">(Contributions</text>
    <text class="segment-note" x="891" y="329">Management</text>
    <text class="segment-note" x="891" y="338">Programs)</text>
    <text class="ring-number" x="952" y="340">12</text>
  </g>

  <!-- Colour palette -->
  <g class="palette">
    <rect x="82" y="527" width="32" height="32" fill="#f7931e"/>
    <rect x="122" y="527" width="32" height="32" fill="#ffdd00"/>
    <rect x="163" y="527" width="32" height="32" fill="#56b04a"/>
    <rect x="204" y="527" width="32" height="32" fill="#00b5b8"/>
    <rect x="245" y="527" width="32" height="32" fill="#29a8e0"/>
    <rect x="82" y="590" width="32" height="32" fill="#e8892a"/>
    <rect x="122" y="590" width="32" height="32" fill="#fcd116"/>
    <rect x="163" y="590" width="32" height="32" fill="#5aa86a"/>
    <rect x="204" y="590" width="32" height="32" fill="#4fc3c4"/>
    <rect x="245" y="590" width="32" height="32" fill="#5cb5e6"/>
    <rect x="82" y="655" width="32" height="32" fill="#64318f"/>
    <rect x="122" y="655" width="32" height="32" fill="#a6192e"/>
    <rect x="163" y="655" width="32" height="32" fill="#2e743a"/>
    <rect x="204" y="655" width="32" height="32" fill="#0f6468"/>
    <rect x="245" y="655" width="32" height="32" fill="#0b4f9c"/>
    <text class="swatch-name" x="247" y="666">Deep Blue</text>
    <rect x="82" y="720" width="32" height="32" fill="#85736a"/>
    <text class="swatch-name" x="84" y="745">Warm Gray</text>
    <rect x="122" y="720" width="32" height="32" fill="#fff6d5"/>
    <rect x="163" y="720" width="32" height="32" fill="#bfcfa1"/>

    <g class="swatch-code">
      <text x="82" y="566">0/50/100/0</text><text x="82" y="571">144 C</text><text x="82" y="576">144 U</text><text x="82" y="581">#F7931E</text>
      <text x="122" y="566">0/10/100/0</text><text x="122" y="571">109 C</text><text x="122" y="576">109 U</text><text x="122" y="581">#FFDD00</text>
      <text x="163" y="566">67/0/95/0</text><text x="163" y="571">361 C</text><text x="163" y="576">361 U</text><text x="163" y="581">#56B04A</text>
      <text x="204" y="566">78/0/33/0</text><text x="204" y="571">326 C</text><text x="204" y="576">326 U</text><text x="204" y="581">#00B5B8</text>
      <text x="245" y="566">100/0/0/0</text><text x="245" y="571">299 C</text><text x="245" y="576">299 U</text><text x="245" y="581">#29A8E0</text>
      <text x="82" y="629">0/55/95/0</text><text x="82" y="634">716 C</text><text x="82" y="639">716 U</text><text x="82" y="644">#E8892A</text>
      <text x="122" y="629">0/17/100/0</text><text x="122" y="634">7406 C</text><text x="122" y="639">7406 U</text><text x="122" y="644">#FCD116</text>
      <text x="163" y="629">65/0/75/0</text><text x="163" y="634">7482 C</text><text x="163" y="639">7482 U</text><text x="163" y="644">#5AA86A</text>
      <text x="204" y="629">65/0/30/0</text><text x="204" y="634">7472 C</text><text x="204" y="639">7472 U</text><text x="204" y="644">#4FC3C4</text>
      <text x="245" y="629">64/11/0/0</text><text x="245" y="634">292 C</text><text x="245" y="639">292 U</text><text x="245" y="644">#5CB5E6</text>
      <text x="82" y="694">76/100/0/0</text><text x="82" y="699">526 C</text><text x="82" y="704">526 U</text><text x="82" y="709">#64318F</text>
      <text x="122" y="694">7/100/67/31</text><text x="122" y="699">7427 C</text><text x="122" y="704">7427 U</text><text x="122" y="709">#A6192E</text>
      <text x="163" y="694">75/10/94/38</text><text x="163" y="699">364 C</text><text x="163" y="704">364 U</text><text x="163" y="709">#2E743A</text>
      <text x="204" y="694">100/10/36/46</text><text x="204" y="699">323 C</text><text x="204" y="704">323 U</text><text x="204" y="709">#0F6468</text>
      <text x="245" y="694">100/72/0/12</text><text x="245" y="699">287 C</text><text x="245" y="704">287 U</text><text x="245" y="709">#0B4F9C</text>
    </g>
  </g>

  <!-- Team structure -->
  <g class="team-structure">
    <line class="scope-divider" x1="407" y1="725" x2="1150" y2="725" stroke="#666" stroke-width="1.2" stroke-dasharray="8 5"/>
    <text class="scope-label" x="697" y="597">Internal</text>
    <text class="scope-label" x="697" y="766">External</text>

    <!-- Medical Products branch -->
    <g class="branch-medical-products" stroke="var(--orange)" stroke-width="1.2" fill="none">
      <polyline points="430,557 430,743 438,743"/>
      <line x1="430" y1="628" x2="438" y2="628"/>
      <line x1="558" y1="557" x2="558" y2="618"/>
    </g>
    <rect x="423" y="505" width="149" height="47" fill="var(--orange)"/>
    <rect x="423" y="552" width="149" height="5" fill="var(--charcoal)"/>
    <text class="division-title" x="497" y="535">Medical Products</text>

    <rect x="438" y="618" width="94" height="20" fill="var(--orange)"/>
    <text class="team-title" x="445" y="632">Medical Affairs</text>
    <rect x="438" y="638" width="94" height="39" fill="var(--charcoal)"/>
    <text class="team-member" x="445" y="655">Marion Hale</text>
    <text class="team-member" x="445" y="667">Celia Warrick</text>

    <rect x="566" y="618" width="94" height="20" fill="var(--orange)"/>
    <text class="team-title" x="573" y="632">Commercial</text>
    <rect x="566" y="638" width="94" height="39" fill="var(--charcoal)"/>
    <text class="team-member" x="573" y="655">Dana Whitfield</text>

    <rect x="438" y="733" width="94" height="20" fill="var(--orange)"/>
    <text class="team-title" x="445" y="747">Medical Affairs</text>
    <rect x="438" y="753" width="94" height="39" fill="var(--charcoal)"/>
    <text class="team-member" x="445" y="770">Karen Ashby</text>
    <text class="team-member" x="445" y="782">Clara Venn</text>

    <!-- Bio Science branch -->
    <g class="branch-bio-science" stroke="var(--blue)" stroke-width="1.2" fill="none">
      <polyline points="884,557 884,743 890,743"/>
      <polyline points="866,645 866,628 890,628"/>
      <line x1="1010" y1="557" x2="1010" y2="628"/>
      <line x1="1010" y1="628" x2="1018" y2="628"/>
    </g>
    <rect x="876" y="505" width="148" height="47" fill="var(--blue)"/>
    <rect x="876" y="552" width="148" height="5" fill="var(--charcoal)"/>
    <text class="division-title" x="950" y="535">Bio Science</text>

    <rect x="795" y="645" width="78" height="21" fill="var(--blue)"/>
    <text class="team-title" x="801" y="660">Clinical Trials</text>
    <rect x="795" y="666" width="78" height="28" fill="var(--charcoal)"/>
    <text class="team-member" x="801" y="683">Joan Albright</text>

    <rect x="890" y="618" width="95" height="20" fill="var(--blue)"/>
    <text class="team-title" x="897" y="632">Medical Affairs</text>
    <rect x="890" y="638" width="95" height="38" fill="var(--charcoal)"/>
    <text class="team-member" x="897" y="655">Ramon Castel</text>

    <rect x="1018" y="618" width="95" height="20" fill="var(--blue)"/>
    <text class="team-title" x="1025" y="632">Commercial</text>
    <rect x="1018" y="638" width="95" height="38" fill="var(--charcoal)"/>
    <text class="team-member" x="1025" y="655">Vera Lindqvist</text>
    <text class="team-member" x="1025" y="667">Nadia Rourke</text>

    <rect x="890" y="733" width="95" height="20" fill="var(--blue)"/>
    <text class="team-title" x="897" y="747">Medical Affairs</text>
    <rect x="890" y="753" width="95" height="38" fill="var(--charcoal)"/>
    <text class="team-member" x="897" y="770">Mina Sadeghi</text>

    <!-- Contributions team -->
    <rect x="638" y="812" width="176" height="20" fill="var(--green)"/>
    <text class="team-title" x="726" y="826" text-anchor="middle">Contibutions Management Team</text>
    <rect x="638" y="832" width="176" height="29" fill="var(--charcoal)"/>
    <text class="team-member" x="726" y="848" text-anchor="middle">Adele Harmon</text>
  </g>
</svg>
</body>
</html>
```